Business card for a new innovative and professional lawn care business

We need a business card design for a new lawn care business in Halifax NS Canada. We offer lawn services in Halifax & Bedford. Our services offered include lawn care, garden services, and property maintenance. We take pride in our work and are experienced at what we do. I would like to see a design that is double sided. On the backside I would like the something simple (maybe my logo preferably on blackround (linked below) with website link, Pagebook page or something). The front I want to include contact info:
Darren Maple
phone 902-555-0148
email - darrensyardworks.ca
facebook - Facebook.com/darrensyardworks
Snapfeed maybe ? - instagram.com/darrenyardworks
Serving Halifax and Bedford for 5 years?
I don't want it to have too much information as I will be passing them out in aim to visit website, or call !
We do want it to include lawn care, garden services and property maintenance.
Basic, catchy, and modern looking !
Logo attached below !

Target Market(s)

Passing business cards to everyone I meet or interact with.

Industry/Entity Type

Lawn Care

Contact Information for Business Card

Double sided with some basic information, with catchy colours and easy to look at.

Font styles to use
Sans Serif

Requirements
Must have
• Must be double sided and have :
• Name, Phone, Email, FB, Website, and 3 main services offered - lawn care, property maintenance, garden services
Nice to have
• Would be nice to have instagram link if it goes well on there
Should not have
• Don't want too much writing or images that are distracting

```html
<!DOCTYPE html>
<html lang="en">
<head>
<meta charset="utf-8">
<title>Darren's Yardworks — Business Card</title>
<link rel="stylesheet" href="https://fonts.googleapis.com/css2?family=Open+Sans:wght@400;600;700;800&display=swap">
<style>
  :root {
    --page: #2b2b2b;
    --card-black: #050505;
    --lime: #8cc63f;
    --forest: #137a3a;
    --white: #ffffff;
    --social-blue: #3b5a9a;
  }
  * { box-sizing: border-box; margin: 0; padding: 0; }
  html, body { width: 1200px; height: 900px; overflow: hidden; }
  body {
    background: var(--page);
    font-family: "Open Sans", Arial, sans-serif;
    display: flex;
    flex-direction: column;
    align-items: center;
    justify-content: center;
    gap: 40px;
  }
  .card {
    position: relative;
    width: 640px;
    height: 366px;
    border-radius: 22px;
    background: var(--card-black);
    overflow: hidden;
  }
  .brand-name {
    font-family: "Open Sans", Arial, sans-serif;
    font-weight: 800;
    color: var(--lime);
    text-transform: uppercase;
    line-height: 1.05;
    letter-spacing: 1px;
  }
  .brand-name .brand-line { display: block; }

  /* back side */
  .card-back .brand {
    position: absolute;
    left: 0; right: 0; top: 96px;
    text-align: center;
  }
  .card-back .brand-name { font-size: 46px; }
  .social-list {
    position: absolute;
    left: 172px; top: 236px;
    list-style: none;
    display: flex; flex-direction: column; gap: 10px;
  }
  .social-item {
    display: flex; align-items: center; gap: 10px;
    color: var(--white); font-size: 17px; font-weight: 600;
  }
  .social-mark {
    width: 14px; height: 14px; border-radius: 2px;
    background: var(--social-blue); flex: none;
  }

  /* front side */
  .card-front .brand {
    position: absolute; left: 48px; top: 128px;
  }
  .card-front .brand-name { font-size: 36px; }
  .front-panel { position: absolute; inset: 0; }
  .contact-block {
    position: absolute; right: 34px; top: 52px;
    text-align: right; color: var(--white);
  }
  .holder-name { font-size: 27px; font-weight: 700; letter-spacing: .5px; margin-bottom: 8px; }
  .contact-line, .service-line {
    display: flex; justify-content: flex-end; align-items: center; gap: 8px;
    font-size: 14.5px; font-weight: 600; line-height: 1.55;
  }
  .contact-icon { width: 13px; height: 13px; flex: none; }
  .services-title { font-size: 19px; font-weight: 800; margin-top: 14px; margin-right: 19px; }
  .service-dot { width: 7px; height: 7px; border-radius: 50%; background: var(--forest); flex: none; margin-left: 4px; }
</style>
</head>
<body>

  <section class="card card-back" aria-label="Card back">
    <div class="brand">
      <p class="brand-name"><span class="brand-line">Darren's</span><span class="brand-line">Yardworks</span></p>
    </div>
    <ul class="social-list">
      <li class="social-item"><span class="social-mark"></span>Pagebook.com/darrensyardworks</li>
      <li class="social-item"><span class="social-mark"></span>snapfeed.com/darrenyardworks</li>
    </ul>
  </section>

  <section class="card card-front" aria-label="Card front">
    <svg class="front-panel" viewBox="0 0 640 366" width="640" height="366" aria-hidden="true">
      <path d="M322 366 C322 180 430 30 560 0 L640 0 L640 366 Z" fill="var(--forest)"/>
      <path d="M344 366 C344 200 450 45 600 0 L640 0 L640 366 Z" fill="var(--lime)"/>
    </svg>

    <div class="brand">
      <p class="brand-name"><span class="brand-line">Darren's</span><span class="brand-line">Yardworks</span></p>
    </div>

    <div class="contact-block">
      <p class="holder-name">DARREN MAPLE</p>
      <p class="contact-line">902-555-0148
        <svg class="contact-icon" viewBox="0 0 16 16"><path d="M4 1 L6.5 4 L5 6 Q6.5 9.5 10 11 L12 9.5 L15 12 L13 15 Q4 14 1 3 Z" fill="var(--forest)"/></svg>
      </p>
      <p class="contact-line">info@darrensyardworks.ca
        <svg class="contact-icon" viewBox="0 0 16 16"><rect x="1" y="3" width="14" height="10" rx="1.5" fill="none" stroke="var(--forest)" stroke-width="1.8"/><path d="M1.5 4 L8 9 L14.5 4" fill="none" stroke="var(--forest)" stroke-width="1.6"/></svg>
      </p>
      <p class="contact-line">www.darrensyardworks.ca
        <svg class="contact-icon" viewBox="0 0 16 16"><circle cx="8" cy="8" r="6.5" fill="none" stroke="var(--forest)" stroke-width="1.6"/><ellipse cx="8" cy="8" rx="2.8" ry="6.5" fill="none" stroke="var(--forest)" stroke-width="1.3"/><path d="M1.5 8 H14.5" stroke="var(--forest)" stroke-width="1.3"/></svg>
      </p>
      <p class="services-title">SERVICES</p>
      <p class="service-line">Lawn care<span class="service-dot"></span></p>
      <p class="service-line">Garden services<span class="service-dot"></span></p>
      <p class="service-line">Property maintenance<span class="service-dot"></span></p>
    </div>
  </section>

</body>
</html>
```